Renewed electronic office supplies

I need a landing page design for a B2B business that will sell refurbished and renewed electronic devices such as smartphones, laptops, tablets and other gadgets. We want to become suppliers of these devices to companies that need computers and other devices for their employees. The point of our business is that they can get a great device that is in very good contrition instead of buying brand new. Companies will be able to save 50-60% on these renewed devices. Not only that we will also buy the companies old devices which they no longe needs and renew them and give them new life so we can resell it.

Our services will be:

- sale of renewed devices with lifetime warranty

- purchase of old devices

- swap solution: meaning client buy from us and sell at the same time so we deduct the amount sale of their old devices into their purchase.

Some useful information:

- company name and logo are still pending

- we aim to provide all business with top quality of renewed and environmentally friendly electronics, while maintaining a minimal impact on the natural environment.

I have attached a word document with some additional info that might be useful

Looking forward to seeing all your great designs!

P.s. Please feel free to make designs that are not based on my documents also, we need different layouts and designs. as for now I see many of the designs are more or less the same. we need more variation on design

Target Market(s)

Medium to large Businesses

Industry/Entity Type

Technology Equipment

Requirements
Must have
• we need more designs to be submitted , 50 designs minimum

```html
<!DOCTYPE html>
<html lang="en">
<head>
<meta charset="UTF-8">
<title>Reusable Electronic Office Supplies</title>
<link rel="stylesheet" href="https://fonts.googleapis.com/css2?family=Poppins:ital,wght@0,400;0,500;0,600;0,700;0,800;1,500&display=swap">
<style>
  :root{
    --blue:#3a9ddb;
    --blue-light:#7cc3ee;
    --blue-deep:#1f6fae;
    --orange:#f7a81b;
    --orange-deep:#f29100;
    --ink:#1f2733;
    --text:#6b7280;
    --white:#ffffff;
    --footer:#232a33;
    --footer-text:#a9b0ba;
  }
  *{box-sizing:border-box;margin:0;padding:0}
  html,body{width:1200px;height:3348px;overflow:hidden;background:var(--white)}
  body{font-family:"Poppins",sans-serif;color:var(--ink)}
  .page{position:relative;width:1200px;height:3348px;overflow:hidden}
  .abs{position:absolute}

  /* hero */
  .hero-bg{left:0;top:0}
  .brand{left:96px;top:38px;display:flex;align-items:center;gap:10px;color:var(--white);font-weight:600;font-size:16px}
  .brand-dot{width:14px;height:14px;border-radius:50%;background:var(--white)}
  .phone-line{left:968px;top:58px;display:flex;align-items:center;gap:10px;font-size:17px;font-weight:600;color:var(--ink)}
  .follow-rail{left:92px;top:150px;display:flex;flex-direction:column;align-items:center;gap:14px}
  .follow-rail .label{writing-mode:vertical-rl;transform:rotate(180deg);color:var(--white);font-size:10px;letter-spacing:3px;opacity:.85}
  .follow-rail .dot{width:12px;height:12px;border-radius:50%;background:var(--white);opacity:.9}
  .hero-copy{left:708px;top:208px;width:430px}
  .hero-title{font-size:35px;line-height:1.2;font-weight:800;color:var(--ink);text-transform:uppercase}
  .hero-text{margin-top:20px;font-size:13px;line-height:1.7;color:var(--text)}
  .btn{display:inline-block;margin-top:58px;background:var(--orange);color:var(--white);font-size:12px;font-weight:600;letter-spacing:1px;padding:12px 36px;border-radius:4px;text-transform:uppercase}

  /* categories */
  .categories{left:88px;top:822px;display:flex;gap:24px}
  .cat{position:relative;width:240px;height:240px}
  .cat-accent{position:absolute;right:-8px;bottom:-8px;width:130px;height:130px;border-right:6px solid var(--orange);border-bottom:6px solid var(--orange);border-radius:0 0 26px 0}
  .cat-media{position:absolute;inset:0;border-radius:22px;overflow:hidden}
  .cat-label{position:absolute;left:0;right:0;bottom:18px;text-align:center;color:var(--white);font-size:15px;font-weight:500}

  /* feature sections */
  .eyebrow{font-size:22px;font-style:italic;font-weight:500;color:var(--blue)}
  .section-title{font-size:34px;line-height:1.22;font-weight:700;color:var(--ink)}
  .section-text{margin-top:22px;font-size:13px;line-height:1.75;color:var(--text)}
  .about{left:90px;top:1250px;width:470px}
  .buy{left:632px;top:1975px;width:470px}
  .sell{left:90px;top:2485px;width:470px}

  /* footer */
  .footer{left:0;top:2960px;width:1200px;height:388px;background:var(--footer);color:var(--footer-text)}
  .f-col{position:absolute;top:62px;font-size:12px;line-height:1.8}
  .f-brand{left:90px;width:260px}
  .f-brand .brand-name{display:flex;align-items:center;gap:10px;color:var(--white);font-size:16px;font-weight:600;margin-bottom:16px}
  .f-brand .brand-dot{background:var(--blue)}
  .f-head{color:var(--white);font-size:14px;font-weight:600;margin-bottom:16px}
  .f-contact{left:430px;width:260px}
  .f-contact li{display:flex;gap:12px;align-items:flex-start;margin-bottom:8px;list-style:none}
  .f-contact svg{flex:none;margin-top:4px}
  .f-services{left:760px}
  .f-services li{list-style:none;margin-bottom:8px}
  .f-follow{left:966px}
  .socials{display:flex;gap:14px}
  .socials span{width:14px;height:14px;border-radius:50%;background:var(--blue)}
  .copyright{position:absolute;left:90px;bottom:26px;font-size:11px;display:flex;align-items:center;gap:10px}
  .copyright .brand-dot{width:10px;height:10px;background:var(--blue)}
</style>
</head>
<body>
<div class="page">

  <svg class="abs hero-bg" width="1200" height="820" viewBox="0 0 1200 820">
    <defs>
      <linearGradient id="heroBlue" x1="0" y1="0" x2="1" y2="1">
        <stop offset="0" stop-color="#4fb0e6"/>
        <stop offset="1" stop-color="#2e8ccc"/>
      </linearGradient>
      <linearGradient id="phoneShot" x1="0" y1="0" x2="1" y2="1">
        <stop offset="0" stop-color="#3a3f47"/>
        <stop offset="1" stop-color="#0f1216"/>
      </linearGradient>
    </defs>
    <path d="M1080 0 H1200 V36 C1170 50 1120 40 1080 0 Z" fill="var(--orange)"/>
    <path d="M0 0 H690 C660 120 690 260 676 420 C662 610 560 780 400 808 C260 830 120 790 0 760 Z" fill="var(--orange)"/>
    <path d="M0 0 H672 C642 120 672 260 658 420 C644 600 548 760 400 788 C260 812 120 772 0 744 Z" fill="url(#heroBlue)"/>
    <path d="M0 300 C200 250 420 330 660 250 L662 330 C420 420 200 330 0 400 Z" fill="var(--blue-light)" opacity=".35"/>
    <path d="M0 520 C180 470 420 560 640 480 L610 560 C420 630 200 560 0 610 Z" fill="var(--blue-light)" opacity=".25"/>
    <g role="img" aria-label="Smartphone with a cracked screen">
      <rect x="170" y="70" width="240" height="500" rx="34" transform="rotate(8 290 320)" fill="url(#phoneShot)"/>
    </g>
  </svg>

  <div class="abs brand"><span class="brand-dot"></span>Logo Goes Here</div>

  <div class="abs follow-rail">
    <span class="label">FOLLOW US</span>
    <span class="dot" style="margin-top:150px"></span>
    <span class="dot"></span>
    <span class="dot"></span>
    <span class="dot"></span>
  </div>

  <div class="abs phone-line">
    <svg width="18" height="18" viewBox="0 0 24 24"><path d="M6.6 10.8a15.2 15.2 0 0 0 6.6 6.6l2.2-2.2a1 1 0 0 1 1-.25 11.4 11.4 0 0 0 3.6.57 1 1 0 0 1 1 1V20a1 1 0 0 1-1 1A17 17 0 0 1 3 4a1 1 0 0 1 1-1h3.5a1 1 0 0 1 1 1c0 1.250.2 2.450.57 3.57a1 1 0 0 1-.25 1z" fill="var(--orange)"/></svg>
    01-555-204-318
  </div>

  <div class="abs hero-copy">
    <h1 class="hero-title">Reusable electronic office supplies</h1>
    <p class="hero-text">We aim to provide all business with top quality of reused and environmentally friendly electronics, while maintaining a minimal impact on the natural environment.</p>
    <span class="btn">Shop</span>
  </div>

  <div class="abs categories">
    <div class="cat">
      <span class="cat-accent"></span>
      <div class="cat-media" role="img" aria-label="Hand holding a smartphone" style="background:linear-gradient(150deg,#3b4250,#111418)"></div>
      <span class="cat-label">Smartphones</span>
    </div>
    <div class="cat">
      <span class="cat-accent"></span>
      <div class="cat-media" role="img" aria-label="Open laptop with glowing screen" style="background:linear-gradient(150deg,#2a1d3a,#0d0a12 70%,#4a2f57)"></div>
      <span class="cat-label">Laptops</span>
    </div>
    <div class="cat">
      <span class="cat-accent"></span>
      <div class="cat-media" role="img" aria-label="Tablet on a desk" style="background:linear-gradient(150deg,#6d7177,#26292d)"></div>
      <span class="cat-label">Tablets</span>
    </div>
    <div class="cat">
      <span class="cat-accent"></span>
      <div class="cat-media" role="img" aria-label="Smartwatch and gadgets" style="background:linear-gradient(150deg,#4f5a66,#1a1f25)"></div>
      <span class="cat-label">Gadgets</span>
    </div>
  </div>

  <svg class="abs" style="left:600px;top:1110px" width="600" height="600" viewBox="0 0 600 600">
    <defs>
      <linearGradient id="aboutShot" x1="0" y1="0" x2="1" y2="1">
        <stop offset="0" stop-color="#6aa3d6"/>
        <stop offset=".55" stop-color="#3b4a5c"/>
        <stop offset="1" stop-color="#1e2a38"/>
      </linearGradient>
    </defs>
    <path d="M40 420 C30 520 120 590 260 580 C380 572 470 540 600 560 V430 C480 470 300 470 200 420 Z" fill="var(--orange)"/>
    <path d="M120 60 C230 0 420 10 600 40 V500 C480 520 330 560 220 530 C110 500 70 420 80 300 C90 190 60 100 120 60 Z" fill="var(--blue)"/>
    <path d="M134 78 C240 22 420 30 600 58 V486 C480 506 330 542 224 514 C122 486 88 414 98 302 C108 196 78 112 134 78 Z" fill="url(#aboutShot)" role="img" aria-label="Technician in blue gloves repairing a circuit board"/>
  </svg>

  <div class="abs about">
    <p class="eyebrow">We are</p>
    <h2 class="section-title">A smarter circular solution for electronic supplies</h2>
    <p class="section-text">Millions of electronics are being made, sold and disposed of every year – a cycle that drives short-term profits for electronics manufacturers, but at too high a cost for the planet we all share. With our experience in the recycling market we can put an end to this cycle and offer a circular solution that is both affordable and environmentally friendly.</p>
  </div>

  <svg class="abs" style="left:0;top:1740px" width="600" height="600" viewBox="0 0 600 600">
    <defs>
      <linearGradient id="buyShot" x1="0" y1="0" x2="1" y2="1">
        <stop offset="0" stop-color="#8aa0ab"/>
        <stop offset=".45" stop-color="#2f4a55"/>
        <stop offset="1" stop-color="#e2763a"/>
      </linearGradient>
    </defs>
    <path d="M300 560 C420 560 560 520 580 400 C600 300 560 200 520 160 L470 420 C420 500 340 520 300 560 Z" fill="var(--orange)"/>
    <path d="M0 40 C140 10 360 0 470 60 C560 110 560 250 540 360 C520 470 430 540 300 556 C190 570 80 560 0 540 Z" fill="var(--blue)"/>
    <path d="M0 58 C140 28 356 18 460 76 C544 122 542 252 522 358 C504 458 420 524 298 538 C190 552 80 544 0 524 Z" fill="url(#buyShot)" role="img" aria-label="Circuit board and multimeter on an orange workbench"/>
  </svg>

  <div class="abs buy">
    <h2 class="section-title">Buy reusable IT</h2>
    <p class="section-text">We specialise in refurbished electronic devices with top quality for all workplace areas. All our products have undergone a detailed testing and reconditioning program by expert technicians.</p>
  </div>

  <svg class="abs" style="left:620px;top:2350px" width="580" height="560" viewBox="0 0 580 560">
    <defs>
      <linearGradient id="sellShot" x1="0" y1="0" x2="1" y2="1">
        <stop offset="0" stop-color="#9fd6f5"/>
        <stop offset=".5" stop-color="#2f86c7"/>
        <stop offset="1" stop-color="#0e3b6b"/>
      </linearGradient>
    </defs>
    <path d="M20 330 C0 440 60 530 200 545 C320 558 440 530 580 520 V440 C430 470 250 460 120 360 Z" fill="var(--orange)"/>
    <path d="M110 40 C220 0 420 10 580 30 V480 C460 500 320 530 200 500 C90 470 50 380 60 260 C70 160 40 70 110 40 Z" fill="var(--blue)"/>
    <path d="M124 58 C230 20 420 28 580 48 V464 C460 484 320 512 204 484 C104 456 70 376 78 262 C88 166 60 86 124 58 Z" fill="url(#sellShot)" role="img" aria-label="Hand holding a tablet with a glowing cloud above it"/>
  </svg>

  <div class="abs sell">
    <h2 class="section-title">Sell your IT Safely</h2>
    <p class="section-text">We can also buy your used electronics and make sure they get wiped and give them a new life. By selling your used devices that you no longer have use for, you can help us create carbon savings.</p>
  </div>

  <footer class="abs footer">
    <div class="f-col f-brand">
      <div class="brand-name"><span class="brand-dot"></span>Logo Goes Here</div>
      <p>Renewed laptops, phones and tablets for growing companies, with a lifetime warranty on every device we supply.</p>
    </div>
    <div class="f-col f-contact">
      <p class="f-head">Contact Info</p>
      <ul>
        <li><svg width="12" height="12" viewBox="0 0 24 24"><path d="M12 2a7 7 0 0 0-7 7c0 5 7 13 7 13s7-8 7-13a7 7 0 0 0-7-7zm0 9.5A2.5 2.5 0 1 1 12 6.5a2.5 2.5 0 0 1 0 5z" fill="var(--orange)"/></svg><span>24 Elm Street, Building 3,<br>Greenfield City</span></li>
        <li><svg width="12" height="12" viewBox="0 0 24 24"><path d="M3 5h18v14H3z M3 5l9 8 9-8" fill="none" stroke="var(--orange)" stroke-width="2"/></svg><span>hello@renewoffice.com</span></li>
        <li><svg width="12" height="12" viewBox="0 0 24 24"><path d="M6.6 10.8a15.2 15.2 0 0 0 6.6 6.6l2.2-2.2a1 1 0 0 1 1-.25 11.4 11.4 0 0 0 3.6.57 1 1 0 0 1 1 1V20a1 1 0 0 1-1 1A17 17 0 0 1 3 4a1 1 0 0 1 1-1h3.5a1 1 0 0 1 1 1c0 1.250.2 2.450.57 3.57a1 1 0 0 1-.25 1z" fill="var(--orange)"/></svg><span>01-555-204-318</span></li>
        <li><svg width="12" height="12" viewBox="0 0 24 24"><circle cx="12" cy="12" r="9" fill="none" stroke="var(--orange)" stroke-width="2"/><path d="M3 12h18M12 3c3 3 3 15 0 18M12 3c-3 3-3 15 0 18" fill="none" stroke="var(--orange)" stroke-width="1.5"/></svg><span>www.renewoffice.com</span></li>
      </ul>
    </div>
    <div class="f-col f-services">
      <p class="f-head">Services</p>
      <ul>
        <li>Smartphones</li>
        <li>Laptops</li>
        <li>Tablets</li>
        <li>Gadgets</li>
      </ul>
    </div>
    <div class="f-col f-follow">
      <p class="f-head">Follow Us</p>
      <div class="socials"><span></span><span></span><span></span><span></span></div>
    </div>
    <p class="copyright"><span class="brand-dot"></span>© 2024 Logo Goes Here. All Rights Reserved.</p>
  </footer>

</div>
</body>
</html>
```